Social Media Overlay for Ormond Real Estate

We need an social media overlay that can be added to a photo of a house that includes our current logo and a call to action of "Just Listed". This needs to be something that we can use for every new house that we list. Attached is our current logo in both company colors, purple and white. An example of a overlay from Plazeo that we like.

Target Market(s)

Social Media Real Estate Community - Real Estate Agents, Brokers, Buyers & Sellers

Industry/Entity Type

Real Estate

Font styles to use
Sans Serif

Colors
6c459b

Requirements
Must have
• the company colors, purple and white and the company logo
Nice to have
• call to action "Just Listed"
• some layered, texture, or 3-D effect
Should not have
• Should be clean and simple; nothing too busy

```html
<!DOCTYPE html>
<html lang="en">
<head>
<meta charset="utf-8">
<title>Just Listed Overlay – Ormond Real Estate</title>
<link rel="stylesheet" href="https://fonts.googleapis.com/css2?family=Montserrat:wght@500;600&family=Poppins:wght@500&display=swap">
<style>
  :root {
    --purple: #5b2b86;
    --purple-text: #6c459b;
    --white: #ffffff;
    --sky-top: #2f8fe0;
    --sky-bottom: #8cc6ef;
    --trees: #3f6a2e;
    --house: #e9e6d8;
    --drive: #e3e1d8;
  }
  html, body {
    margin: 0;
    padding: 0;
    width: 1200px;
    height: 1200px;
    overflow: hidden;
    background: var(--white);
  }
  .canvas {
    position: relative;
    width: 1200px;
    height: 1200px;
    overflow: hidden;
  }
  .listing-photo {
    position: absolute;
    inset: 0;
    background:
      linear-gradient(180deg,
        var(--sky-top) 0%,
        var(--sky-bottom) 18%,
        var(--trees) 30%,
        #58803c 42%,
        var(--house) 52%,
        #d8d2c2 70%,
        var(--drive) 80%,
        #cfcdc4 100%);
  }
  .just-listed {
    position: absolute;
    left: 535px;
    top: 878px;
    width: 325px;
    height: 322px;
    box-sizing: border-box;
    background: var(--purple);
    border: 5px solid var(--white);
    border-radius: 62px;
    box-shadow: 0 0 0 2px var(--purple);
    display: flex;
    flex-direction: column;
    justify-content: center;
    align-items: center;
    z-index: 2;
  }
  .just-listed span {
    font-family: "Montserrat", sans-serif;
    font-weight: 500;
    color: var(--white);
    font-size: 82px;
    line-height: 1.12;
    letter-spacing: 1px;
  }
  .brand-tab {
    position: absolute;
    left: 830px;
    top: 935px;
    width: 400px;
    height: 190px;
    box-sizing: border-box;
    background: var(--white);
    border: 5px solid var(--purple);
    border-radius: 55px;
    display: flex;
    flex-direction: column;
    justify-content: center;
    padding-left: 62px;
    z-index: 1;
  }
  .brand-name {
    font-family: "Poppins", sans-serif;
    font-weight: 500;
    color: var(--purple-text);
    font-size: 58px;
    line-height: 1;
  }
  .brand-sub {
    font-family: "Poppins", sans-serif;
    font-weight: 500;
    color: var(--purple-text);
    font-size: 36px;
    line-height: 1.2;
    margin-top: 4px;
  }
</style>
</head>
<body>
  <main class="canvas">
    <div class="listing-photo" role="img" aria-label="Photo of the listed house: two-storey home with stone accents, tall trees, blue sky and a wide driveway"></div>
    <div class="brand-tab">
      <div class="brand-name">Ormond</div>
      <div class="brand-sub">Real Estate</div>
    </div>
    <div class="just-listed">
      <span>JUST</span>
      <span>LISTED</span>
    </div>
  </main>
</body>
</html>
```